New Business Card Design Project

Bloom of the Willow Wellness Clinic PLLC
Bloomofthewillowwc-example.com
Board Certified Nursing Coach in life, health, & wellness.
Hypnotherapy, weight loss & vitamin supplement injections, IV hydration.
Offering mobile clinics

```html
<!DOCTYPE html>
<html lang="en">
<head>
<meta charset="utf-8">
<title>Bloom of the Willow Wellness Clinic – Business Card</title>
<link rel="stylesheet" href="https://fonts.googleapis.com/css2?family=Roboto:wght@400;500;700&display=swap">
<style>
  :root {
    --bg: #2b2b2d;
    --card: #1d1e20;
    --card-edge: #26272a;
    --orange: #f08a24;
    --orange-deep: #e2571c;
    --gold: #f6b042;
    --cream: #f3e3c8;
    --text: #f4f4f4;
    --rule: #bdbdbd;
    --pattern: #2a2b2e;
  }
  * { box-sizing: border-box; margin: 0; padding: 0; }
  html, body { width: 1200px; height: 1107px; overflow: hidden; }
  body {
    background: var(--bg);
    font-family: "Roboto", Arial, sans-serif;
    display: flex;
    align-items: center;
    justify-content: center;
    gap: 70px;
  }
  .card {
    width: 460px;
    height: 700px;
    background: var(--card);
    border-radius: 22px;
    position: relative;
    overflow: hidden;
    box-shadow: 0 18px 40px rgba(0,0,0,.45);
  }

  /* Front */
  .card-front {
    display: flex;
    flex-direction: column;
    align-items: center;
    padding-top: 70px;
    color: var(--text);
    text-align: center;
  }
  .brand-mark {
    display: flex;
    flex-direction: column;
    align-items: center;
    gap: 22px;
    height: 300px;
    justify-content: center;
  }
  .brand-mark .dot {
    width: 120px; height: 120px; border-radius: 50%;
    background: var(--orange);
  }
  .brand-mark .brand-name {
    font-weight: 500; font-size: 22px; color: var(--orange);
    letter-spacing: .5px;
  }
  .person-name {
    margin-top: 48px;
    font-size: 30px; font-weight: 700; color: var(--orange);
    letter-spacing: .5px;
  }
  .person-role { font-size: 22px; margin-top: 2px; }
  .icon-row {
    display: flex; align-items: center; gap: 10px;
    width: 340px; margin-top: 16px;
  }
  .icon-row .rule { flex: 1; height: 1px; background: var(--rule); }
  .icon {
    width: 34px; height: 34px; border-radius: 6px;
    background: linear-gradient(160deg, var(--gold), var(--orange-deep));
    display: flex; align-items: center; justify-content: center;
  }
  .contact { margin-top: 10px; font-size: 21px; line-height: 1.3; }
  .divider { width: 340px; height: 1px; background: var(--rule); margin: 12px 0; }
  .address { font-size: 21px; line-height: 1.3; }

  /* Back */
  .card-back { display: flex; flex-direction: column; align-items: center; }
  .pattern-field {
    position: absolute; inset: 0;
    background: radial-gradient(circle at 50% 40%, var(--pattern), var(--card) 80%);
  }
  .back-brand {
    position: absolute; left: 0; right: 0; top: 440px;
    display: flex; flex-direction: column; align-items: center; gap: 14px;
  }
  .back-brand .dot { width: 56px; height: 56px; border-radius: 50%; background: var(--orange); }
  .back-brand .brand-name {
    font-weight: 500; font-size: 26px; color: var(--orange);
    letter-spacing: 1px; text-align: center; line-height: 1.3;
  }
  .back-brand .rule { width: 260px; height: 1px; background: var(--orange); }
</style>
</head>
<body>
  <article class="card card-front">
    <div class="brand-mark">
      <span class="dot"></span>
      <span class="brand-name">Bloom of the Willow</span>
    </div>
    <h1 class="person-name">DANIEL CARTER</h1>
    <p class="person-role">Managing Director</p>
    <div class="icon-row">
      <span class="rule"></span>
      <span class="icon" aria-label="Phone">
        <svg width="20" height="20" viewBox="0 0 24 24"><path d="M6.6 10.8a15 15 0 0 0 6.6 6.6l2.2-2.2c.3-.3.7-.4 1-.2 1.1.4 2.3.6 3.6.6.6 0 1 .4 1 1V20c0 .6-.4 1-1 1A17 17 0 0 1 3 4c0-.6.4-1 1-1h3.5c.6 0 1 .4 1 1 0 1.3.2 2.5.6 3.6.1.3 0 .7-.2 1z" fill="#1d1e20"/></svg>
      </span>
      <span class="icon" aria-label="Email">
        <svg width="20" height="20" viewBox="0 0 24 24"><rect x="3" y="6" width="18" height="12" rx="1" fill="none" stroke="#1d1e20" stroke-width="2"/><path d="M3 7l9 6 9-6" fill="none" stroke="#1d1e20" stroke-width="2"/></svg>
      </span>
      <span class="icon" aria-label="Website">
        <svg width="20" height="20" viewBox="0 0 24 24"><circle cx="12" cy="12" r="9" fill="none" stroke="#1d1e20" stroke-width="2"/><path d="M3 12h18M12 3c3 3 3 15 0 18M12 3c-3 3-3 15 0 18" fill="none" stroke="#1d1e20" stroke-width="1.5"/></svg>
      </span>
      <span class="rule"></span>
    </div>
    <p class="contact">044-555 010 200<br>info@example-mail.com<br>Bloomofthewillowwc-example.com</p>
    <span class="divider"></span>
    <p class="address">Your Address, City<br>State, Zip 0000</p>
  </article>

  <article class="card card-back">
    <div class="pattern-field" role="img" aria-label="Tonal spot-gloss pattern of repeated brand motifs"></div>
    <div class="back-brand">
      <span class="dot"></span>
      <span class="rule"></span>
      <p class="brand-name">BLOOM OF THE WILLOW<br>WELLNESS CLINIC</p>
      <span class="rule"></span>
    </div>
  </article>
</body>
</html>
```